Quarrydeen Fintech Product Infographic

Quarrydeen is an established Fintech business, supplying complex financial software to banks and building societies.

We currently have a picture/infographic to show each of our 11 different software products in a single image. Each product can be installed on its own as a standalone application or if multiple products are installed they will share data.

The key message for our infographic is to convey the integration via a shared database.

The attached diagram is what we currently use which is to give you an idea of the message we are trying to give, but we are not tied to this format and are looking for this diagram to be reimagined.

We will look to use our new chosen design on printed media such as A4 Data sheets an example of which is attached.

For more information on our products please refer to www.quarrydeen.co.uk/products

```html
<!DOCTYPE html>
<html lang="en">
<head>
<meta charset="utf-8">
<title>Quarrydeen Fintech Product Infographic</title>
<link rel="stylesheet" href="https://fonts.googleapis.com/css2?family=Mulish:wght@400;600;700&display=swap">
<style>
  :root {
    --finance-band: #4dbbeb;
    --finance-a: #45b1e2;
    --finance-b: #38a8da;
    --finance-c: #2c9fd0;
    --regulatory-band: #68c18f;
    --regulatory-a: #5dbb84;
    --regulatory-b: #50b577;
    --regulatory-c: #35a862;
    --risk-band: #fbbb53;
    --risk-a: #f0a140;
    --risk-b: #fbb851;
    --performance-band: #c27db5;
    --performance-a: #ab5f9d;
    --performance-b: #b86ca7;
    --performance-c: #c079b2;
    --hub-light: #1f5c8c;
    --hub-dark: #263a78;
    --label: #ffffff;
    --canvas: #ffffff;
  }
  html, body {
    margin: 0;
    padding: 0;
    width: 1200px;
    height: 849px;
    overflow: hidden;
    background: var(--canvas);
  }
  .product-wheel {
    display: block;
    width: 1200px;
    height: 849px;
    font-family: "Mulish", sans-serif;
  }
  .group-title {
    fill: var(--label);
    font-size: 27px;
    font-weight: 400;
    letter-spacing: 1.5px;
  }
  .product-name {
    fill: var(--label);
    font-size: 22px;
    font-weight: 700;
    text-anchor: middle;
  }
  .hub-title {
    fill: var(--label);
    font-size: 18px;
    font-weight: 600;
    text-anchor: middle;
  }
  .divider {
    stroke: var(--canvas);
    stroke-width: 8;
  }
</style>
</head>
<body>
<svg class="product-wheel" viewBox="0 0 1200 849" xmlns="http://www.w3.org/2000/svg" aria-label="Quarrydeen products sharing one database">
  <defs>
    <path id="quadrant" d="M0,0 L-277.9,-277.9 A393,393 0 0 1 277.9,-277.9 Z"/>
    <path id="slice-third" d="M0,0 L-84.1,-313.9 A325,325 0 0 1 84.1,-313.9 Z"/>
    <path id="slice-half" d="M0,0 L-124.4,-300.3 A325,325 0 0 1 124.4,-300.3 Z"/>
    <path id="arc-finance" d="M345.4,170.4 A360,360 0 0 1 854.6,170.4"/>
    <path id="arc-regulatory" d="M854.6,679.6 A360,360 0 0 0 854.6,170.4"/>
    <path id="arc-risk" d="M345.4,679.6 A360,360 0 0 0 854.6,679.6"/>
    <path id="arc-performance" d="M345.4,170.4 A360,360 0 0 0 345.4,679.6"/>
    <linearGradient id="hub-fill" x1="0" y1="0" x2="1" y2="1">
      <stop offset="0" stop-color="var(--hub-light)"/>
      <stop offset="1" stop-color="var(--hub-dark)"/>
    </linearGradient>
  </defs>

  <g transform="translate(600 425)">
    <!-- outer bands -->
    <use href="#quadrant" fill="var(--finance-band)"/>
    <use href="#quadrant" fill="var(--regulatory-band)" transform="rotate(90)"/>
    <use href="#quadrant" fill="var(--risk-band)" transform="rotate(180)"/>
    <use href="#quadrant" fill="var(--performance-band)" transform="rotate(270)"/>

    <!-- finance products -->
    <use href="#slice-third" fill="var(--finance-a)" transform="rotate(-30)"/>
    <use href="#slice-third" fill="var(--finance-b)"/>
    <use href="#slice-third" fill="var(--finance-c)" transform="rotate(30)"/>
    <!-- regulatory products -->
    <use href="#slice-third" fill="var(--regulatory-a)" transform="rotate(60)"/>
    <use href="#slice-third" fill="var(--regulatory-b)" transform="rotate(90)"/>
    <use href="#slice-third" fill="var(--regulatory-c)" transform="rotate(120)"/>
    <!-- risk products -->
    <use href="#slice-half" fill="var(--risk-b)" transform="rotate(157.5)"/>
    <use href="#slice-half" fill="var(--risk-a)" transform="rotate(202.5)"/>
    <!-- performance products -->
    <use href="#slice-third" fill="var(--performance-c)" transform="rotate(240)"/>
    <use href="#slice-third" fill="var(--performance-b)" transform="rotate(270)"/>
    <use href="#slice-third" fill="var(--performance-a)" transform="rotate(300)"/>

    <!-- dividers between groups -->
    <line class="divider" x1="0" y1="0" x2="0" y2="-400" transform="rotate(45)"/>
    <line class="divider" x1="0" y1="0" x2="0" y2="-400" transform="rotate(135)"/>
    <line class="divider" x1="0" y1="0" x2="0" y2="-400" transform="rotate(225)"/>
    <line class="divider" x1="0" y1="0" x2="0" y2="-400" transform="rotate(315)"/>

    <!-- shared data hub -->
    <circle r="102" fill="var(--canvas)"/>
    <circle r="94" fill="url(#hub-fill)"/>
  </g>

  <rect x="553" y="343" width="94" height="84" rx="10" fill="#3f5aa8" opacity="0.55" role="img" aria-label="Illustration of database servers"/>
  <text class="hub-title" x="600" y="471">SHARED</text>
  <text class="hub-title" x="600" y="492">DATA</text>

  <!-- group titles -->
  <text class="group-title" dominant-baseline="middle"><textPath href="#arc-finance" startOffset="50%" text-anchor="middle">FINANCE</textPath></text>
  <text class="group-title" dominant-baseline="middle"><textPath href="#arc-regulatory" startOffset="50%" text-anchor="middle">REGULATORY</textPath></text>
  <text class="group-title" dominant-baseline="middle"><textPath href="#arc-risk" startOffset="50%" text-anchor="middle">RISK</textPath></text>
  <text class="group-title" dominant-baseline="middle"><textPath href="#arc-performance" startOffset="50%" text-anchor="middle">PERFORMANCE</textPath></text>

  <!-- product names -->
  <text class="product-name" transform="translate(486 218) rotate(60)"><tspan x="0" y="-4">Financial</tspan><tspan x="0" y="22">Ledgers</tspan></text>
  <text class="product-name"><tspan x="600" y="160">Effective</tspan><tspan x="600" y="186">Interest</tspan><tspan x="600" y="212">Rates</tspan></text>
  <text class="product-name" transform="translate(711 232) rotate(-60)"><tspan x="0" y="-4">Hedge</tspan><tspan x="0" y="22">Accounting</tspan></text>

  <text class="product-name" transform="translate(794 318) rotate(-30)"><tspan x="0" y="-4">Regulatory</tspan><tspan x="0" y="22">Reporting</tspan></text>
  <text class="product-name"><tspan x="833" y="420">Taxation</tspan><tspan x="833" y="447">Reporting</tspan></text>
  <text class="product-name" transform="translate(807 543) rotate(30)"><tspan x="0" y="8">FSCS SCV</tspan></text>

  <text class="product-name" x="515" y="633">Treasury</text>
  <text class="product-name" x="684" y="637">ALM</text>

  <text class="product-name" transform="translate(390 314) rotate(30)"><tspan x="0" y="-4">Financial</tspan><tspan x="0" y="22">Planning</tspan></text>
  <text class="product-name"><tspan x="385" y="420">Funds Transfer</tspan><tspan x="385" y="447">Pricing</tspan></text>
  <text class="product-name" transform="translate(411 536) rotate(-30)"><tspan x="0" y="-4">Business</tspan><tspan x="0" y="22">Intelligence</tspan></text>
</svg>
</body>
</html>
```